Long Established Local Fencing (not swords) Business needs fresh Business Cards

We need fresh double sided business cards for our Fencing Construction business, we are looking for something with our new logo design added, and maybe a photo background ?
We recently had cards made from Quillmarko and we were horrified with what we got back, the quality was terrible, so am looking for high quality format for good printing company to make.
We install Steelwave, Timber paling, Aluminium Slat Screening, Picket (timber and aluminium) and most other fencing installations.
Our website is brelbanfencing.com.au should you like to learn a bit more.
We do have logo in other formats if required.
We have been in business for over 35 years and we have used this as a "motto" it is on our signage

Industry/Entity Type

Construction

Contact Information for Business Card

Open to ideas, we need 3 x different cards, one generic with no name and 2 x others each with 1 of our bosses name on each, I will put into upload files.

Colors
ec1f27
000000
606060
f5f5f5

Requirements
Must have
• Company Name and Logo
• Address
• Contact details, phone, website, email etc
• Small space to write notes when leaving card at residence
Nice to have
• Our motto "Servicing the Peninsula for over 35 years"

```html
<!DOCTYPE html>
<html lang="en">
<head>
<meta charset="utf-8">
<title>Brelban Fencing – Business Card</title>
<link href="https://fonts.googleapis.com/css2?family=Roboto:ital,wght@0,400;0,700;1,400&family=Roboto+Condensed:wght@700&display=swap" rel="stylesheet">
<style>
  :root {
    --brand-red: #e0302f;
    --ink: #000000;
    --grey: #606060;
    --text: #4a4a4a;
    --paper: #f5f5f5;
    --backdrop: #2a2a2a;
  }
  * { margin: 0; padding: 0; box-sizing: border-box; }
  html, body {
    width: 1200px; height: 960px; overflow: hidden;
    background: var(--backdrop);
    font-family: "Roboto", Arial, sans-serif;
  }
  .card {
    position: absolute; left: 313px;
    width: 600px; height: 343px;
    background: var(--paper);
    box-shadow: 0 2px 6px rgba(0,0,0,0.5);
    overflow: hidden;
  }
  .card--front { top: 113px; }
  .card--back { top: 472px; }

  .brand-panel {
    position: absolute; left: 0; top: 0;
    width: 190px; height: 100%;
    background: var(--brand-red);
    display: flex; align-items: center; justify-content: center;
  }
  .brand-panel__name {
    color: #ffffff;
    font-family: "Roboto Condensed", Arial, sans-serif;
    font-weight: 700; font-size: 26px; line-height: 1.1;
    text-align: center; letter-spacing: 1px;
  }

  .details {
    position: absolute; right: 37px; top: 137px;
    text-align: right; color: var(--text);
  }
  .details__name {
    font-family: "Roboto Condensed", Arial, sans-serif;
    font-weight: 700; font-size: 21px; color: var(--brand-red);
    margin-bottom: 8px; letter-spacing: 0.3px;
  }
  .details__line { font-size: 14.5px; line-height: 18px; }
  .contacts { margin-top: 12px; }
  .contact {
    display: flex; justify-content: flex-end; align-items: center;
    font-size: 14.5px; line-height: 19px; margin-right: -22px;
  }
  .contact svg { width: 12px; height: 12px; margin-left: 7px; fill: var(--brand-red); }

  .wordmark {
    position: absolute; top: 38px; left: 0; width: 100%;
    display: flex; justify-content: center; align-items: center; gap: 10px;
  }
  .wordmark__dot { width: 18px; height: 18px; border-radius: 50%; background: var(--brand-red); }
  .wordmark__name {
    font-family: "Roboto Condensed", Arial, sans-serif;
    font-weight: 700; font-size: 28px; color: var(--ink); letter-spacing: 1px;
  }
  .notes { position: absolute; left: 48px; top: 130px; width: 500px; }
  .notes__line { height: 35px; border-bottom: 1px dotted #555; }
  .notes__line:first-child { height: 0; }
  .motto {
    position: absolute; left: 0; top: 302px; width: 100%;
    text-align: center; font-style: italic; font-size: 14px; color: var(--text);
  }
</style>
</head>
<body>
  <section class="card card--front">
    <div class="brand-panel">
      <div class="brand-panel__name">BRELBAN<br>FENCING</div>
    </div>
    <div class="details">
      <div class="details__name">DARREN KELLOW</div>
      <div class="details__line">42 Marlo St Brelban</div>
      <div class="details__line">License No: 52164k</div>
      <div class="details__line">ABN 41 582 93 106</div>
      <div class="contacts">
        <div class="contact">(02)45550182
          <svg viewBox="0 0 24 24"><path d="M6.6 10.8a15 15 0 0 0 6.6 6.6l2.2-2.2a1 1 0 0 1 1-.25 11.4 11.4 0 0 0 3.6.6 1 1 0 0 1 1 1V20a1 1 0 0 1-1 1A17 17 0 0 1 3 4a1 1 0 0 1 1-1h3.5a1 1 0 0 1 1 1c0 1.25.2 2.45.6 3.6a1 1 0 0 1-.25 1z"/></svg>
        </div>
        <div class="contact">0491 570 236
          <svg viewBox="0 0 24 24"><path d="M7 1h10a2 2 0 0 1 2 2v18a2 2 0 0 1-2 2H7a2 2 0 0 1-2-2V3a2 2 0 0 1 2-2zm0 3v14h10V4z"/></svg>
        </div>
        <div class="contact">brelbanfencing@netmail.com
          <svg viewBox="0 0 24 24"><path d="M2 5h20v14H2zm2 2v.5l8 5 8-5V7l-8 5z"/></svg>
        </div>
        <div class="contact">www.brelbanfencing.com.au
          <svg viewBox="0 0 24 24"><circle cx="12" cy="12" r="10"/></svg>
        </div>
      </div>
    </div>
  </section>

  <section class="card card--back">
    <div class="wordmark">
      <span class="wordmark__dot"></span>
      <span class="wordmark__name">BRELBAN FENCING</span>
    </div>
    <div class="notes">
      <div class="notes__line"></div>
      <div class="notes__line"></div>
      <div class="notes__line"></div>
      <div class="notes__line"></div>
      <div class="notes__line"></div>
    </div>
    <p class="motto">Servicing the Peninsula for over 35 years</p>
  </section>
</body>
</html>
```